Business Card Design for a Private Label Pet Company

We need a business card design for our family-owned company, Hollow Creek Pet Works (www.hollowcreekpetworks.com), out of St. Louis, MO. We provide turnkey private label solutions for retailers, Marketvale sellers and other brands who want to provide high quality, natural, Made in the USA pet products to their customers. Our customer are worldwide and range from the US to the UK to Vietnam and beyond. We offer private label for dozens of pet products including grooming products (shampoos, conditioners, colognes, ear and eye washes, mouthwash, etc.), all meat treats, supplements, and specialty products (pet stain and odor cleaner, anti-chew spray, etc.). We would like to see designs that use the colors, fonts and logos (see variations) within our brand guidelines and fit with the look and feel from our website.

Target Market(s)

Pet Store Owners, Marketvale Sellers, Pet Brand Marketers

Industry/Entity Type

Pet

Contact Information for Business Card

Tom Willoughby
CEO
Hollow Creek Pet Works
5817 Brookhaven Commerce Lane
St. Louis, MO 63521
office: 314.555.0182
mobile: 770.555.0139
email: tom@hollowcreekpetworks.com

Colors

Designer to choose colors to be used in the design.

Requirements
Must have
• Need to follow the brand guidelines attached for colors, fonts and logos
• Need to use the logos attached (or a variation) with our without the tagline
• Name, title, phone (office and mobil), email, address on the business card
• Clean professional look and feel that says: high quality natural pet products, high quality service, made in the USA
Nice to have
• Made in the USA is a big positive in our industry and we are very proud of it. There is an attached icon from our website. The designer can get creative here as they wish.
• I do like using color for pop. Just don't like lots of bright, loud colors.
Should not have
• lots of bright, loud colors
• overwhelming to the reader
• crowded

```html
<!DOCTYPE html>
<html lang="en">
<head>
<meta charset="utf-8">
<title>Hollow Creek Pet Works – Business Card</title>
<link href="https://fonts.googleapis.com/css2?family=Roboto:wght@400;500;700&display=swap" rel="stylesheet">
<style>
  :root {
    --backdrop: #e9e6e1;
    --paper: #f7f7f6;
    --slate-teal: #4a5f5d;
    --leaf-green: #6b8a2f;
    --ink: #4c4f51;
    --rule: #c9cbcb;
    --reverse-text: #f2f3f2;
  }
  * { margin: 0; padding: 0; box-sizing: border-box; }
  html, body {
    width: 1200px; height: 960px; overflow: hidden;
    background: var(--backdrop);
    font-family: "Roboto", Arial, sans-serif;
  }
  .canvas { position: relative; width: 1200px; height: 960px; }

  .card { position: absolute; width: 600px; height: 343px; }

  /* Front */
  .card-front { left: 314px; top: 113px; background: var(--paper); overflow: hidden; }
  .front-wordmark {
    position: absolute; left: 0; top: 0; width: 296px; height: 325px;
    display: flex; flex-direction: column; align-items: center; justify-content: center;
  }
  .wordmark-line {
    font-weight: 700; font-size: 29px; line-height: 1.08;
    letter-spacing: 0.5px; text-transform: uppercase; color: var(--slate-teal);
  }
  .divider {
    position: absolute; left: 296px; top: 82px; width: 1px; height: 192px;
    background: var(--rule);
  }
  .contact { position: absolute; left: 321px; top: 82px; color: var(--ink); }
  .contact-name {
    font-weight: 500; font-size: 21px; color: var(--slate-teal);
    text-transform: uppercase; line-height: 22px;
  }
  .contact-title { font-size: 15px; color: var(--leaf-green); line-height: 20px; }
  .contact-address { margin-top: 12px; font-size: 14.5px; line-height: 18px; }
  .contact-lines { margin-top: 8px; list-style: none; font-size: 14.5px; line-height: 19px; }
  .contact-lines li { display: flex; align-items: center; gap: 9px; }
  .contact-lines svg { width: 13px; height: 13px; fill: var(--ink); flex: none; }
  .band-accent {
    position: absolute; left: 0; top: 324px; width: 100%; height: 2px; background: var(--leaf-green);
  }
  .band-base {
    position: absolute; left: 0; top: 328px; width: 100%; height: 15px; background: var(--slate-teal);
  }

  /* Back */
  .card-back { left: 312px; top: 472px; background: var(--slate-teal); }
  .back-wordmark {
    position: absolute; left: 0; top: 120px; width: 100%;
    display: flex; flex-direction: column; align-items: center;
  }
  .back-wordmark .wordmark-line { color: var(--reverse-text); font-size: 34px; }
  .back-url {
    position: absolute; left: 0; top: 286px; width: 100%; text-align: center;
    font-size: 14px; letter-spacing: 3.4px; color: var(--reverse-text);
  }
</style>
</head>
<body>
<main class="canvas">

  <section class="card card-front" aria-label="Business card front">
    <div class="front-wordmark">
      <span class="wordmark-line">Hollow Creek</span>
      <span class="wordmark-line">Pet Works</span>
    </div>
    <div class="divider"></div>
    <div class="contact">
      <p class="contact-name">Tom Willoughby</p>
      <p class="contact-title">CEO</p>
      <p class="contact-address">Hollow Creek Pet Works<br>5817 Brookhaven Commerce Lane<br>St. Louis, MO 63521</p>
      <ul class="contact-lines">
        <li>
          <svg viewBox="0 0 24 24" aria-hidden="true"><path d="M6.6 10.8c1.4 2.8 3.8 5.1 6.6 6.6l2.2-2.2c.3-.3.7-.4 1-.2 1.1.4 2.3.6 3.6.6.6 0 1 .4 1 1V20c0 .6-.4 1-1 1C10.6 21 3 13.4 3 4c0-.6.4-1 1-1h3.5c.6 0 1 .4 1 1 0 1.3.2 2.5.6 3.6.1.3 0 .7-.2 1l-2.3 2.2z"/></svg>
          314.555.0182
        </li>
        <li>
          <svg viewBox="0 0 24 24" aria-hidden="true"><path d="M7 1h10c1.1 0 2 .9 2 2v18c0 1.1-.9 2-2 2H7c-1.1 0-2-.9-2-2V3c0-1.1.9-2 2-2zm0 3v14h10V4H7zm5 15.5a1 1 0 100 2 1 1 0 000-2z"/></svg>
          770.555.0139
        </li>
        <li>
          <svg viewBox="0 0 24 24" aria-hidden="true"><path d="M2 5h20v14H2V5zm2 2v.4l8 5 8-5V7H4zm16 2.8l-8 5-8-5V17h16V9.8z"/></svg>
          tom@hollowcreekpetworks.com
        </li>
        <li>
          <svg viewBox="0 0 24 24" aria-hidden="true"><path d="M12 2a10 10 0 100 20 10 10 0 000-20zm-1 17.9A8 8 0 014.1 10L9 15v1c0 1.1.9 2 2 2v1.9zm6.9-2.5c-.3-.8-1-1.4-1.9-1.4h-1v-3c0-.6-.4-1-1-1H8v-2h2c.6 0 1-.4 1-1V7h2c1.1 0 2-.9 2-2v-.4a8 8 0 012.9 12.8z"/></svg>
          hollowcreekpetworks.com
        </li>
      </ul>
    </div>
    <div class="band-accent"></div>
    <div class="band-base"></div>
  </section>

  <section class="card card-back" aria-label="Business card back">
    <div class="back-wordmark">
      <span class="wordmark-line">Hollow Creek</span>
      <span class="wordmark-line">Pet Works</span>
    </div>
    <p class="back-url">www.hollowcreekpetworks.com</p>
  </section>

</main>
</body>
</html>
```